High end Desks & Chairs Distibutor looking for a brochure desin

Bright Haven G.P, Canadian Furniture and Stationery Distributor, (very attractive patented design -mainly Desks & Chairs-), Adjstable to fit many needs.
3 folds flyer,
Bilangual text and photos provided,
Use same colors as Logo
Flyer Disign shoul reflect Ergonomy, High End User Freindly Products, Eco Freindly materials,

Target Market(s)

Limited mobility people
Children from 4 to 17 years old
Multi porpuses desks users

Industry/Entity Type

Distributor

Requirements
Nice to have
• Have a hint for Ergonomic, Adjustable, multi-purpose use.

```html
<!DOCTYPE html>
<html lang="en">
<head>
<meta charset="utf-8">
<title>Bright Haven – Tri-fold Brochure</title>
<link rel="stylesheet" href="https://fonts.googleapis.com/css2?family=Oswald:wght@500;600;700&family=Ubuntu:wght@400;500;700&display=swap">
<style>
  :root {
    --red: #e8171f;
    --ink: #1e1b1c;
    --plum: #7b1c4e;
    --gold: #f3b21b;
    --paper: #ffffff;
    --mist: #eef0f2;
    --stripe: #9a9a9a;
  }
  * { margin: 0; padding: 0; box-sizing: border-box; }
  html, body { width: 873px; height: 1200px; overflow: hidden; background: var(--paper); }
  body { position: relative; font-family: "Ubuntu", sans-serif; color: var(--ink); }

  .sheet { position: absolute; width: 688px; height: 472px; background: var(--paper);
           box-shadow: 0 4px 14px rgba(0,0,0,.22); overflow: hidden; }
  .sheet--outside { left: 113px; top: 88px; }
  .sheet--inside { left: 110px; top: 601px; }
  .sheet__shapes { position: absolute; inset: 0; }
  .fold { position: absolute; top: 0; bottom: 0; width: 30px; pointer-events: none; }
  .fold--a { left: 214px; background: linear-gradient(90deg, rgba(0,0,0,0), rgba(0,0,0,.08) 50%, rgba(0,0,0,0)); }
  .fold--b { left: 444px; background: linear-gradient(90deg, rgba(0,0,0,0), rgba(0,0,0,.08) 50%, rgba(0,0,0,0)); }

  .abs { position: absolute; }
  .media { position: absolute; }

  /* brand name */
  .brand { position: absolute; display: flex; align-items: center; gap: 6px;
           font-family: "Ubuntu", sans-serif; font-weight: 500; white-space: nowrap; }
  .brand__mark { width: 14px; height: 14px; background: var(--gold); }
  .brand--plum { color: var(--plum); }
  .brand--white { color: #fff; }
  .brand--white .brand__mark { background: #fff; }

  /* outside, panel 1 */
  .badge { position: absolute; width: 100px; text-align: center; }
  .badge__icon { width: 36px; height: 36px; margin: 0 auto 5px; }
  .badge__title { font-family: "Oswald", sans-serif; font-weight: 600; font-size: 11.5px; letter-spacing: .3px; line-height: 1.1; }
  .badge__sub { font-size: 6.5px; line-height: 1.2; text-transform: uppercase; }
  .intro__title { left: 17px; top: 110px; font-family: "Oswald", sans-serif; font-weight: 600;
                  font-size: 17px; color: var(--red); }
  .intro__list { left: 17px; top: 143px; width: 190px; list-style: none; font-size: 7.6px; line-height: 10px; }
  .intro__list li { position: relative; padding-left: 10px; margin-bottom: 7px; }
  .intro__list li::before { content: ""; position: absolute; left: 0; top: 3px; width: 4px; height: 4px;
                            border-radius: 50%; background: var(--red); }

  /* outside, panel 2 */
  .pitch { position: absolute; left: 261px; top: 214px; width: 170px; height: 170px; border-radius: 50%;
           background: #fff; box-shadow: 0 2px 6px rgba(0,0,0,.25); display: flex; flex-direction: column;
           align-items: center; justify-content: center; text-align: center; color: var(--ink); line-height: 1.08; }
  .pitch__bold { font-family: "Oswald", sans-serif; font-weight: 600; font-size: 17px; }
  .pitch__light { font-family: "Ubuntu", sans-serif; font-size: 17px; }
  .pitch__wide { font-family: "Oswald", sans-serif; font-weight: 500; font-size: 16px; letter-spacing: 2px; }
  .phone { left: 229px; width: 230px; top: 396px; text-align: center; font-family: "Oswald", sans-serif;
           font-weight: 600; font-size: 25px; color: #fff; letter-spacing: .5px; }
  .web { top: 434px; width: 230px; text-align: center; font-size: 8.4px; color: #fff; letter-spacing: 1.4px; }
  .web--mid { left: 229px; }
  .web--right { left: 458px; }

  /* outside, panel 3 */
  .cover__title { left: 458px; width: 230px; text-align: center; top: 302px; line-height: 1; }
  .cover__line1 { font-family: "Oswald", sans-serif; font-weight: 600; font-size: 42px; color: var(--ink); letter-spacing: .5px; }
  .cover__line2 { font-family: "Oswald", sans-serif; font-weight: 600; font-size: 36px; color: #fff; letter-spacing: .5px; margin-top: 2px; }
  .cover__line3 { font-size: 14.5px; color: #fff; margin-top: 4px; }

  /* inside */
  .copy { position: absolute; width: 204px; color: #fff; font-size: 7.3px; line-height: 9.6px; }
  .copy p { margin-bottom: 9px; }
  .points { position: absolute; width: 204px; display: flex; gap: 10px; color: #fff; font-size: 7.2px; line-height: 9.6px; }
  .points ul { list-style: none; width: 97px; }
  .points li { position: relative; padding-left: 10px; margin-bottom: 3px; }
  .points li::before { content: ""; position: absolute; left: 0; top: 2.5px; width: 4.5px; height: 4.5px;
                       border-radius: 50%; background: var(--ink); }
</style>
</head>
<body>

<!-- OUTSIDE SPREAD -->
<section class="sheet sheet--outside">
  <svg class="sheet__shapes" width="688" height="472" viewBox="0 0 688 472">
    <defs>
      <linearGradient id="room" x1="0" y1="0" x2="1" y2="1">
        <stop offset="0" stop-color="#ffffff"/>
        <stop offset="1" stop-color="#eceeef"/>
      </linearGradient>
    </defs>
    <rect x="0" y="0" width="458" height="472" fill="url(#room)"/>
    <polygon points="0,383 459,243 688,236 688,246 459,253 0,393" fill="#c9c9c9"/>
    <polygon points="0,392 459,252 688,246 688,253 459,259 0,399" fill="var(--ink)"/>
    <polygon points="0,399 459,259 688,253 688,472 0,472" fill="var(--red)"/>
  </svg>

  <div class="badge" style="left:6px; top:30px;">
    <svg class="badge__icon" viewBox="0 0 36 36" aria-hidden="true">
      <circle cx="18" cy="18" r="17" fill="var(--red)"/>
      <circle cx="18" cy="18" r="14" fill="none" stroke="#fff" stroke-width="1"/>
      <path d="M9 11h3l2.5 10h10l2-7H13" fill="none" stroke="#fff" stroke-width="1.8" stroke-linejoin="round"/>
      <circle cx="15.5" cy="24.5" r="1.5" fill="#fff"/><circle cx="23" cy="24.5" r="1.5" fill="#fff"/>
    </svg>
    <div class="badge__title">HIGH END</div>
    <div class="badge__sub">User freindly products</div>
  </div>
  <div class="badge" style="left:122px; top:30px;">
    <svg class="badge__icon" viewBox="0 0 36 36" aria-hidden="true">
      <circle cx="18" cy="18" r="17" fill="var(--red)"/>
      <circle cx="18" cy="18" r="14" fill="none" stroke="#fff" stroke-width="1"/>
      <path d="M17 18c-6 0-8-4-7-9 5 0 8 3 7 9z" fill="#fff"/>
      <path d="M19 18c6 0 8-4 7-9-5 0-8 3-7 9z" fill="#fff"/>
      <path d="M18 19c0 4-2 7-5 8 3 1 6-1 7-4 1 3 4 5 7 4-3-1-5-4-5-8z" fill="#fff"/>
    </svg>
    <div class="badge__title">ECO FREINDLY</div>
    <div class="badge__sub">Materials</div>
  </div>

  <h2 class="abs intro__title">WE ARE</h2>
  <ul class="abs intro__list">
    <li>Bright Haven G.P.</li>
    <li>Canadian Furniture and Stationery Distributor (very attractive patented design -mainly Desks &amp; Chairs-)</li>
    <li>Adjstable to fit many needs.</li>
  </ul>

  <div class="media" role="img" aria-label="Height-adjustable wooden-top desk on a white pedestal base"
       style="left:30px; top:222px; width:190px; height:214px; background:linear-gradient(180deg,#e3c08a 0%,#e9d2ad 25%,#f1f1f1 45%,#e2e4e6 100%); border-radius:4px;"></div>

  <div class="brand brand--plum" style="left:290px; top:128px; font-size:14px;">
    <span class="brand__mark"></span>Bright Haven
  </div>

  <div class="pitch">
    <div class="pitch__bold">VERY ATTRACTIVE</div>
    <div class="pitch__light">patented design</div>
    <div class="pitch__wide">MAINLY</div>
    <div class="pitch__bold">DESKS &amp; CHAIRS</div>
  </div>

  <div class="abs phone">0198 765 432</div>
  <div class="abs web web--mid">www.brighthaven-desks.ca</div>

  <div class="brand brand--plum" style="left:502px; top:52px; font-size:17px;">
    <span class="brand__mark"></span>Bright Haven
  </div>
  <div class="media" role="img" aria-label="Parent and children working together at adjustable desks in a bright room"
       style="left:459px; top:77px; width:229px; height:166px; background:linear-gradient(135deg,#f3efe6 0%,#d9cbb8 45%,#9fb7c9 75%,#c9d8a8 100%);"></div>

  <div class="abs cover__title">
    <div class="cover__line1">CANADIAN</div>
    <div class="cover__line2">FURNITURE</div>
    <div class="cover__line3">and Stationery Distributor</div>
  </div>
  <div class="abs web web--right">www.brighthaven-desks.ca</div>

  <div class="fold fold--a"></div>
  <div class="fold fold--b"></div>
</section>

<!-- INSIDE SPREAD -->
<section class="sheet sheet--inside">
  <svg class="sheet__shapes" width="688" height="472" viewBox="0 0 688 472">
    <polygon points="0,246 459,106 688,104 688,112 459,114 0,254" fill="#c9c9c9"/>
    <polygon points="0,254 459,114 688,112 688,119 459,121 0,261" fill="var(--ink)"/>
    <polygon points="0,261 459,121 688,119 688,472 0,472" fill="var(--red)"/>
    <rect x="0" y="445" width="688" height="27" fill="var(--ink)"/>
  </svg>

  <div class="media" role="img" aria-label="White drafting desk with tilted top on a pedestal base"
       style="left:16px; top:24px; width:170px; height:170px; background:linear-gradient(180deg,#f4f5f6,#dfe2e5); border-radius:4px;"></div>
  <div class="media" role="img" aria-label="White children's desk with split tilting top"
       style="left:252px; top:18px; width:194px; height:152px; background:linear-gradient(180deg,#f4f5f6,#dfe2e5); border-radius:4px;"></div>
  <div class="media" role="img" aria-label="White adjustable desk with flat top"
       style="left:502px; top:16px; width:170px; height:84px; background:linear-gradient(180deg,#f4f5f6,#dfe2e5); border-radius:4px;"></div>

  <div class="copy" style="left:8px; top:269px;">
    <p>Et est putent contentiones. No mel nullam vocent reformidans, pro ea audiam denique, fabulas molestiae eu mel. Cu rebum doming mea, molestiae eloquentiam appellantur no sit. Ut graeco denique vix, solum error lucilius ei his, eam sumo zril tincidunt an. At vis novum accumsan facilisis, sit ex laudem aperiri delicata, brute mazim eripuit duo at.</p>
  </div>
  <div class="points" style="left:8px; top:342px;">
    <ul><li>Eu nam reque atqui mea ad nostrud perfecto</li><li>Partem quaeque omittantur cu ius</li><li>Ea has habemus appellantur</li><li>Omnes soluta quaerendum his an</li></ul>
    <ul><li>Eum deleniti luptatum rationibus eu</li><li>No sea odio eligendi Mel ei nihil homero</li><li>Eu numquam alienum omittam duo</li><li>Feugait repudiandae signiferumque est an</li></ul>
  </div>

  <div class="copy" style="left:239px; top:190px;">
    <p>Eu nam reque atqui, mea ad nostrud perfecto. Partem quaeque omittantur cu ius, ea has habemus appellantur. Omnes soluta quaerendum his an, eum deleniti luptatum rationibus eu, no sea odio eligendi. Mel ei nihil homero, eu numquam alienum omittam duo. Feugait repudiandae signiferumque est an.</p>
    <p>Et est putent contentiones. No mel nullam vocent reformidans, pro ea audiam denique, fabulas molestiae eu mel. Cu rebum doming mea, molestiae eloquentiam appellantur no sit. Ut graeco denique vix, solum error lucilius ei his, eam sumo zril tincidunt an. At vis novum accumsan facilisis, sit ex laudem aperiri delicata, brute mazim eripuit duo at.</p>
  </div>
  <div class="points" style="left:239px; top:342px;">
    <ul><li>Eu nam reque atqui mea ad nostrud perfecto</li><li>Partem quaeque omittantur cu ius</li><li>Ea has habemus appellantur</li><li>Omnes soluta quaerendum his an</li></ul>
    <ul><li>Eum deleniti luptatum rationibus eu</li><li>No sea odio eligendi Mel ei nihil homero</li><li>Eu numquam alienum omittam duo</li><li>Feugait repudiandae signiferumque est an</li></ul>
  </div>

  <div class="copy" style="left:473px; top:137px;">
    <p>Eu nam reque atqui, mea ad nostrud perfecto. Partem quaeque omittantur cu ius, ea has habemus appellantur. Omnes soluta quaerendum his an, eum deleniti luptatum rationibus eu, no sea odio eligendi. Mel ei nihil homero, eu numquam alienum omittam duo. Feugait repudiandae signiferumque est an.</p>
    <p>Et est putent contentiones. No mel nullam vocent reformidans, pro ea audiam denique, fabulas molestiae eu mel. Cu rebum doming mea, molestiae eloquentiam appellantur no sit. Ut graeco denique vix, solum error lucilius ei his, eam sumo zril tincidunt an. At vis novum accumsan facilisis, sit ex laudem aperiri delicata, brute mazim eripuit duo at.</p>
  </div>
  <div class="points" style="left:473px; top:289px;">
    <ul><li>Eu nam reque atqui mea ad nostrud perfecto</li><li>Partem quaeque omittantur cu ius</li><li>Ea has habemus appellantur</li><li>Omnes soluta quaerendum his an</li></ul>
    <ul><li>Eum deleniti luptatum rationibus eu</li><li>No sea odio eligendi Mel ei nihil homero</li><li>Eu numquam alienum omittam duo</li><li>Feugait repudiandae signiferumque est an</li></ul>
  </div>

  <div class="brand brand--white" style="left:516px; top:414px; font-size:14px;">
    <span class="brand__mark"></span>Bright Haven
  </div>

  <div class="fold fold--a" style="left:214px;"></div>
  <div class="fold fold--b" style="left:444px;"></div>
</section>

</body>
</html>
```